IT Freelancer (Consulting, trainer and project manager) needed letterhead

As a freelancer for IT Trainingswhip, consulting and project management I need a letterhead design. What is desired is a design that fits the existing logo (see Annex). It is functional, reliable, and equal time wirkenn Agil and modern. The whole is in color, as well as printed out to make a good impression on a black and white printer. The whole is to the existing Cooperate design (business card, homepage, logo) fit. Therefore, the choice of colors.

Target Market(s)

Customers such as medium-sized enterprises, training institutions

Industry/Entity Type

Consulting

Colors
0455a3
3277b5
85abd2
cfdfed
34a6d7
32a6d6
249fd4
0792cd
85cae6

Requirements
Must have
• Must include logo (see Annex) address (Ahornweg 14, 84317 Kastelried, Germany). Must seriously and act simultaneously Agil. Design should (even) be adaptable (signature, address, etc.) design must look good on a black / white laser

```html
<!DOCTYPE html>
<html lang="de">
<head>
<meta charset="utf-8">
<title>Markus Feldner – Briefbogen</title>
<link rel="stylesheet" href="https://fonts.googleapis.com/css2?family=Montserrat:wght@700&family=Arimo:wght@400&display=swap">
<style>
  :root {
    --paper: #f6f6f6;
    --paper-shade: #e9e9e9;
    --band-light: #dcdcdc;
    --band-mid: #c4c4c4;
    --rule: #6f6f6f;
    --mark: #5f5f5f;
    --ink: #555555;
    --address: #5a5a5a;
  }
  * { margin: 0; padding: 0; box-sizing: border-box; }
  html, body { width: 849px; height: 1200px; overflow: hidden; background: #ffffff; }
  .letterhead {
    position: relative;
    width: 849px;
    height: 1200px;
    overflow: hidden;
    background: var(--paper);
  }
  .paper-texture {
    position: absolute;
    inset: 0;
    background:
      radial-gradient(ellipse at 45% 35%, #ffffff 0%, rgba(255,255,255,0) 60%),
      linear-gradient(180deg, var(--paper) 0%, var(--paper-shade) 100%);
  }
  .frame-shapes {
    position: absolute;
    inset: 0;
    width: 849px;
    height: 1200px;
  }
  .brand-dot {
    position: absolute;
    left: 117px;
    top: 33px;
    width: 142px;
    height: 142px;
    border-radius: 50%;
    background: var(--mark);
    box-shadow: 0 0 0 8px #ffffff;
  }
  .brand-name {
    position: absolute;
    left: 47px;
    top: 204px;
    width: 280px;
    text-align: center;
    font-family: "Montserrat", sans-serif;
    font-weight: 700;
    color: var(--ink);
    line-height: 1;
  }
  .brand-name .first {
    display: block;
    font-size: 35px;
    letter-spacing: 1px;
  }
  .brand-name .last {
    display: block;
    margin-top: 6px;
    font-size: 27px;
    letter-spacing: 10px;
    padding-left: 10px;
  }
  .sender-address {
    position: absolute;
    left: 438px;
    top: 1113px;
    font-family: "Arimo", sans-serif;
    font-size: 16.5px;
    color: var(--address);
    white-space: nowrap;
  }
</style>
</head>
<body>
  <main class="letterhead">
    <div class="paper-texture" role="img" aria-label="Feines geschwungenes Liniengitter als heller Hintergrund"></div>

    <svg class="frame-shapes" viewBox="0 0 849 1200" aria-hidden="true">
      <polygon points="230,0 849,0 849,146 264,146" fill="var(--band-light)"/>
      <polygon points="0,0 310,0 0,250" fill="var(--band-mid)"/>
      <rect x="264" y="140" width="585" height="7" fill="var(--rule)"/>
      <polygon points="0,1068 849,1146 849,1200 0,1200" fill="var(--band-mid)"/>
      <polygon points="380,1156 849,1156 849,1200 560,1200" fill="var(--band-light)"/>
      <rect x="376" y="1146" width="473" height="6" fill="var(--rule)"/>
    </svg>

    <span class="brand-dot"></span>
    <h1 class="brand-name">
      <span class="first">MARKUS</span>
      <span class="last">FELDNER</span>
    </h1>

    <footer class="sender-address">Ahornweg 14, 84317 Kastelried,Nordland</footer>
  </main>
</body>
</html>
```